VORK.
BRIDGING HORIZONS
VORK. -
Creative Brief
Use specific fonts
any thing which suits with the LOGO provided
Professional
RAJESH MOTLA
MR.
B.P. No.6213, COMMUNE-3, NEAR TORAVI LAUNDRY, KALEBA ZONE, BAMAKO-MALI
rajesh@vork.co.in
vork.co.in
pls mention MANAGING DIRECTOR, the designation, below the name of the person.
LOGO at centre. Below mentioned address at bottom: India Office D-47, Palm Enclave-II, Gurgaon, Haryana 122015 ph:+91-124-4708352, fax:+91-124-4519267 cell:+91-9871436029

```html
<!DOCTYPE html>
<html lang="en">
<head>
<meta charset="utf-8">
<title>VORK. Stationery Set</title>
<link href="https://fonts.googleapis.com/css2?family=Montserrat:wght@400;600;700&display=swap" rel="stylesheet">
<style>
:root{
  --board:#3a3b3d;
  --paper:#ffffff;
  --navy:#0c2f6b;
  --blue:#1a63b8;
  --teal:#1c8f8a;
  --green:#7cc242;
  --ink:#2a2f38;
  --muted:#8a9099;
  --rule:#dfe3e8;
  --faint:#e9eef4;
  --caption:#a9adb2;
}
*{margin:0;padding:0;box-sizing:border-box}
html,body{width:1200px;height:312px;overflow:hidden;background:var(--board);font-family:"Montserrat",Arial,sans-serif}
.board{position:relative;width:1200px;height:312px}
.item{position:absolute;background:var(--paper);box-shadow:0 2px 6px rgba(0,0,0,.45);overflow:hidden}
.edge{position:absolute;left:0;top:0;bottom:0;width:6px;background:linear-gradient(180deg,var(--navy),var(--blue) 45%,var(--teal) 75%,var(--green))}
.brand{position:absolute;display:flex;align-items:center;gap:3px;font-weight:700;color:var(--navy);letter-spacing:.5px;line-height:1}
.brand .dot{border-radius:50%;background:var(--green);flex:none}
.tagline{position:absolute;font-size:3.2px;color:var(--muted);letter-spacing:.6px;font-weight:600;white-space:nowrap}
.caption{position:absolute;font-size:4.5px;color:var(--caption);letter-spacing:.3px;text-align:center}

/* business cards */
.card{width:82px;height:48px}
.card .brand{left:12px;top:10px;font-size:8px}
.card .brand .dot{width:6px;height:6px}
.card-front .tagline{left:21px;top:21px;font-size:2.8px}
.card-back .brand{font-size:6px;top:7px}
.card-back .brand .dot{width:4.5px;height:4.5px}
.person{position:absolute;left:12px;top:18px;line-height:1.3}
.person b{display:block;font-size:3.4px;color:var(--navy)}
.person span{display:block;font-size:2.6px;color:var(--muted)}
.card-back .details{position:absolute;left:12px;top:30px;width:64px;font-size:2.4px;line-height:3.4px;color:var(--ink)}

/* letterheads */
.letterhead{width:206px;height:274px;top:19px}
.letterhead .brand{left:18px;top:14px;font-size:12px}
.letterhead .brand .dot{width:8px;height:8px}
.letterhead .tagline{left:30px;top:28px}
.letterhead .contact{position:absolute;right:12px;top:12px;width:84px;text-align:right;font-size:2.8px;line-height:3.8px;color:var(--muted)}
.letterhead .watermark{position:absolute;right:18px;bottom:44px;font-size:30px;font-weight:700;color:var(--faint);letter-spacing:1px}
.letterhead .footer{position:absolute;left:0;right:0;bottom:8px;text-align:center;font-size:2.8px;color:var(--muted)}

/* DL envelopes */
.dl{width:206px;height:101px;left:684px}
.dl .brand{left:14px;top:12px;font-size:10px}
.dl .brand .dot{width:7px;height:7px}
.dl .tagline{left:24px;top:23px}
.dl .to{position:absolute;left:90px;top:58px;width:90px}
.dl .to i{display:block;height:1px;background:var(--rule);margin-bottom:6px}

/* flap envelopes */
.flap-env{position:absolute;left:936px;width:240px}
</style>
</head>
<body>
<main class="board">

  <!-- business cards -->
  <section class="item card card-front" style="left:29px;top:113px">
    <div class="edge"></div>
    <div class="brand"><span class="dot"></span>VORK.</div>
    <div class="tagline">BRIDGING HORIZONS</div>
  </section>
  <section class="item card card-back" style="left:125px;top:113px">
    <div class="edge"></div>
    <div class="brand"><span class="dot"></span>VORK.</div>
    <div class="person"><b>Full Name</b><span>Job Title</span></div>
    <div class="details">Office address line one<br>Phone and email line</div>
  </section>
  <section class="item card card-front" style="left:29px;top:185px">
    <div class="edge"></div>
    <div class="brand"><span class="dot"></span>VORK.</div>
    <div class="tagline">BRIDGING HORIZONS</div>
  </section>
  <section class="item card card-back" style="left:125px;top:185px">
    <div class="edge"></div>
    <div class="brand"><span class="dot"></span>VORK.</div>
    <div class="person"><b>Full Name</b><span>Job Title</span></div>
    <div class="details">Office address line one<br>Phone and email line</div>
  </section>

  <!-- letterheads -->
  <section class="item letterhead" style="left:233px">
    <div class="edge"></div>
    <div class="brand"><span class="dot"></span>VORK.</div>
    <div class="tagline">BRIDGING HORIZONS</div>
    <div class="contact">Street address line<br>City and postal code<br>Phone and fax line<br>Email and web</div>
    <div class="watermark">VORK.</div>
    <div class="footer">Office address and contact line</div>
  </section>
  <div class="caption" style="left:233px;top:296px;width:206px">Letterhead Front</div>

  <section class="item letterhead" style="left:456px">
    <div class="edge"></div>
    <div class="brand"><span class="dot"></span>VORK.</div>
    <div class="tagline">BRIDGING HORIZONS</div>
    <div class="watermark">VORK.</div>
    <div class="footer">Office address and contact line</div>
  </section>
  <div class="caption" style="left:456px;top:296px;width:206px">Letterhead Second</div>

  <!-- DL envelopes -->
  <section class="item dl" style="top:36px">
    <div class="edge"></div>
    <div class="brand"><span class="dot"></span>VORK.</div>
    <div class="tagline">BRIDGING HORIZONS</div>
    <div class="to"><i></i><i></i><i></i></div>
  </section>
  <div class="caption" style="left:684px;top:140px;width:206px">Envelope Front</div>
  <section class="item dl" style="top:158px">
    <div class="edge"></div>
    <div class="brand"><span class="dot"></span>VORK.</div>
    <div class="tagline">BRIDGING HORIZONS</div>
    <div class="to"><i></i><i></i><i></i></div>
  </section>
  <div class="caption" style="left:684px;top:262px;width:206px">Envelope Back</div>

  <!-- flap envelopes, stacked -->
  <svg class="flap-env" style="top:29px;height:70px" viewBox="0 0 240 70" aria-hidden="true">
    <defs><radialGradient id="flapBlue" cx="50%" cy="50%" r="65%"><stop offset="0" stop-color="#3fa7c9"/><stop offset=".5" stop-color="#1a63b8"/><stop offset="1" stop-color="#0c2f6b"/></radialGradient></defs>
    <rect width="240" height="70" fill="url(#flapBlue)"/>
  </svg>
  <svg class="flap-env" style="top:88px;height:64px" viewBox="0 0 240 64" aria-hidden="true">
    <defs><radialGradient id="flapGreen" cx="50%" cy="40%" r="65%"><stop offset="0" stop-color="#c9ec5a"/><stop offset=".5" stop-color="#6fb33c"/><stop offset="1" stop-color="#1f5e2a"/></radialGradient></defs>
    <rect width="240" height="64" fill="url(#flapGreen)"/>
  </svg>
  <svg class="flap-env" style="top:144px;height:128px" viewBox="0 0 240 128" aria-hidden="true">
    <rect width="240" height="128" fill="#fff"/>
    <polygon points="0,0 240,0 120,46" fill="#f1f3f5"/>
    <polyline points="0,0 120,46 240,0" fill="none" stroke="#d6dade"/>
    <line x1="0" y1="60" x2="240" y2="60" stroke="#e3e6ea"/>
  </svg>
  <div class="caption" style="left:936px;top:278px;width:240px">Envelope Set</div>

</main>
</body>
</html>
```